Velmora Biz Card 2019

New business card for Velmora Property Inspections. We are a residential home inspection company in Arizona.

Target Market(s)

Real Estate

Font styles to use
Sans Serif

Requirements
Must have
• Glen Mirewick
• Home Inspector
• Velmora Property Inspections, LLC
• 480-555-0172
• glen@velmora-llc.example

```html
<!DOCTYPE html>
<html lang="en">
<head>
<meta charset="utf-8">
<title>Velmora Business Card</title>
<link rel="stylesheet" href="https://fonts.googleapis.com/css2?family=Open+Sans:wght@400;600;700&display=swap">
<style>
  :root {
    --brand-green: #4cb748;
    --brand-grey: #6d6e71;
    --ink: #3a3a3a;
    --paper: #ffffff;
    --stage: #e9ebea;
    --photo-top: #e4e7ea;
    --photo-bottom: #2b3448;
  }
  * { box-sizing: border-box; margin: 0; padding: 0; }
  html, body {
    width: 1200px; height: 892px; overflow: hidden;
    background: var(--stage);
    font-family: "Open Sans", Arial, sans-serif;
  }
  .stage {
    width: 1200px; height: 892px;
    display: flex; flex-direction: column; align-items: center; justify-content: center;
    gap: 36px;
  }
  .card {
    width: 665px; height: 380px; position: relative; overflow: hidden;
    box-shadow: 0 6px 18px rgba(0,0,0,.18);
  }
  /* back side */
  .card-back { background: var(--brand-green); }
  .back-brand {
    position: absolute; right: 40px; bottom: 70px;
    display: flex; align-items: center; gap: 10px;
    color: var(--paper); font-weight: 700; font-size: 30px; letter-spacing: 2px;
  }
  .brand-square { width: 22px; height: 22px; flex: none; }
  .card-back .brand-square { background: var(--paper); }
  .back-web {
    position: absolute; right: 40px; bottom: 40px;
    color: var(--paper); font-size: 15px;
  }
  /* front side */
  .card-front { background: var(--paper); }
  .portrait {
    position: absolute; left: 120px; top: 120px; width: 290px; height: 260px;
    background: linear-gradient(180deg, var(--photo-top) 0%, var(--photo-top) 40%, var(--photo-bottom) 66%, var(--photo-bottom) 100%);
  }
  .front-brand {
    position: absolute; right: 40px; top: 66px;
    display: flex; align-items: center; gap: 12px;
    color: var(--brand-grey); font-weight: 700; font-size: 38px; letter-spacing: 3px; line-height: 1.1;
  }
  .front-brand .brand-square { background: var(--brand-green); }
  .company-line {
    position: absolute; right: 40px; top: 116px;
    color: var(--brand-grey); font-size: 12px; letter-spacing: .3px;
  }
  .identity {
    position: absolute; right: 40px; top: 148px; text-align: right;
  }
  .person-name {
    color: var(--brand-green); font-weight: 700; font-size: 21px; text-transform: uppercase; line-height: 1.15;
  }
  .person-title {
    color: var(--brand-grey); font-size: 14px; text-transform: uppercase; letter-spacing: .5px;
  }
  .address {
    margin-top: 12px; color: var(--ink); font-size: 14px; line-height: 1.4;
  }
  .contact-band {
    position: absolute; left: 0; right: 0; top: 292px; height: 40px;
    background: var(--brand-green); color: var(--paper);
    display: flex; align-items: center; justify-content: flex-end; padding-right: 30px;
    font-size: 15px; gap: 6px; white-space: nowrap;
  }
  .contact-band b { font-weight: 700; margin-left: 6px; }
</style>
</head>
<body>
<main class="stage">
  <section class="card card-back" aria-label="Card back">
    <div class="back-brand"><span class="brand-square"></span>VELMORA</div>
    <p class="back-web">www.velmora-llc.example</p>
  </section>

  <section class="card card-front" aria-label="Card front">
    <div class="portrait" role="img" aria-label="Portrait photo of Glen Mirewick in a dark navy polo shirt"></div>
    <div class="front-brand"><span class="brand-square"></span>VELMORA</div>
    <p class="company-line">Velmora Property Inspections, LLC</p>
    <div class="identity">
      <p class="person-name">Glen Mirewick</p>
      <p class="person-title">Home Inspector</p>
      <p class="address">2170 Larkspur Lane<br>Mesa Vista, AZ 85201</p>
    </div>
    <div class="contact-band">
      <b>P:</b> 480 555 0172 <b>M:</b> 480 555 0196 <b>E:</b> glen@velmora-llc.example
    </div>
  </section>
</main>
</body>
</html>
```